Re-design casino and gambling website ( no php need )

I'm the owner of website mirvexa3.com and I want to renovate my website following my attachment .

Please note . Only programmer and designer who have ever design casino / gambling website will accept .

```html
<!DOCTYPE html>
<html lang="th">
<head>
<meta charset="utf-8">
<title>MIRVEXA3</title>
<link rel="stylesheet" href="https://fonts.googleapis.com/css2?family=Kanit:wght@300;400;500;600&family=Poppins:wght@300;400;500;600;700&display=swap">
<style>
:root{
  --bg-top:#130d1f;
  --bg-header:#160e24;
  --bg-dark:#000000;
  --bg-footer:#0e0a24;
  --nav-tile:#2a2140;
  --nav-tile-2:#1e1730;
  --panel:#2a2733;
  --card:#221f29;
  --register:#3a2b56;
  --submit:#b2245f;
  --cta:#112a3b;
  --cta-border:#b7343c;
  --accent:#e34b2e;
  --blue:#2b6cf2;
  --demo-blue:#1f8db6;
  --demo-grey:#626268;
  --board:#2a2044;
  --text:#ffffff;
  --muted:#d9d6e2;
  --link:#4d7fe6;
}
*{box-sizing:border-box;margin:0;padding:0}
html,body{width:1200px;height:1147px;overflow:hidden;background:var(--bg-dark)}
body{font-family:"Poppins","Kanit",sans-serif;color:var(--text);position:relative}
.abs{position:absolute}

.topbar{left:0;top:0;width:1200px;height:36px;background:var(--bg-top);font-size:12px;color:var(--muted)}
.topbar .contact{left:66px;top:10px}
.topbar .social{right:66px;top:12px;display:flex;gap:32px}
.topbar .social span{width:9px;height:9px;border-radius:50%;background:var(--muted);display:block}

.header{left:0;top:36px;width:1200px;height:131px;background:var(--bg-header)}
.brand{left:66px;top:24px}
.brand .mark{display:flex;align-items:center;gap:8px;font-size:45px;font-weight:700;color:var(--accent);line-height:1}
.brand .mark i{width:38px;height:38px;border-radius:50%;background:var(--text);display:block}
.brand .url{font-size:16px;font-weight:600;margin-top:6px}

.nav{left:601px;top:19px;display:flex;gap:2px;height:92px}
.nav a{position:relative;display:block;height:92px;background:linear-gradient(180deg,var(--nav-tile),var(--nav-tile-2));text-align:center;color:var(--text);text-decoration:none;padding-top:18px}
.nav .num{font-size:34px;font-weight:600;color:rgba(255,255,255,.35);line-height:1;display:block;height:22px;overflow:hidden}
.nav .en{font-size:13px;display:block;margin-top:2px}
.nav .th{font-family:"Kanit",sans-serif;font-size:12px;display:block;margin-top:4px}

.hero{left:73px;top:167px;width:1127px;height:396px;background:
  radial-gradient(ellipse at 62% 50%,rgba(190,60,80,.55),transparent 55%),
  radial-gradient(ellipse at 25% 45%,rgba(120,50,170,.7),transparent 60%),
  linear-gradient(90deg,#0d0818 0%,#3a1e52 20%,#5a2247 50%,#3b2444 75%,#2a1d38 100%)}
.hero-copy{left:554px;top:137px;width:480px;text-align:center}
.hero-copy .th{font-family:"Kanit",sans-serif;font-size:31px;font-weight:500;line-height:1.3}
.hero-copy .en{font-size:33px;font-weight:600;line-height:1.2;margin-top:-2px}
.btn-signin{display:inline-block;margin-top:6px;background:var(--blue);color:var(--text);font-size:17px;padding:5px 14px;border-radius:2px}

.register{left:80px;top:517px;width:238px;height:163px;background:var(--register);border-radius:8px}
.register h2{position:absolute;left:10px;top:6px;font-family:"Kanit",sans-serif;font-size:25px;font-weight:500;color:var(--accent)}
.register .field{position:absolute;left:9px;width:144px;height:28px;background:#fff;border-radius:3px;color:#888;font-family:"Kanit",sans-serif;font-size:14px;padding:3px 8px;white-space:nowrap;overflow:hidden}
.register .submit{position:absolute;left:162px;top:42px;width:68px;height:91px;background:var(--submit);text-align:center;font-size:14px;padding-top:24px;line-height:1.4}
.register .submit small{font-family:"Kanit",sans-serif;font-size:13px;display:block}
.register .forgot{position:absolute;left:9px;top:136px;font-size:13px;color:var(--link);white-space:nowrap}
.register .forgot span{color:var(--text)}

.cta{left:89px;width:221px;height:80px;background:var(--cta);border:2px solid var(--cta-border);text-align:center;font-size:14px;padding-top:20px;line-height:1.5}
.cta small{font-family:"Kanit",sans-serif;font-size:13px;display:block}

.games{left:333px;top:563px;width:800px;height:374px;background:linear-gradient(180deg,#34313b,var(--panel))}
.game-card{left:19px;width:497px;height:158px;background:var(--card);border:1px solid #34303d;border-radius:6px}
.game-card .thumb{position:absolute;left:12px;top:10px;width:139px;height:100px;background:linear-gradient(135deg,#3a3a3a,#111 70%);border:1px solid #555}
.game-card .num{position:absolute;left:178px;top:14px;font-size:28px;font-weight:600;color:rgba(255,255,255,.5);line-height:1;height:18px;overflow:hidden}
.game-card .th{position:absolute;left:178px;top:32px;font-family:"Kanit",sans-serif;font-size:13px}
.game-card .tag{position:absolute;right:10px;top:30px;font-size:13px;letter-spacing:.5px}
.game-card p{position:absolute;left:178px;top:50px;width:300px;height:64px;overflow:hidden;font-size:13.5px;line-height:21px}
.game-card .btns{position:absolute;left:178px;top:120px;display:flex;gap:3px}
.btn-demo{height:34px;padding:0 12px;font-size:16px;line-height:34px;display:flex;align-items:center;gap:5px}
.btn-demo.primary{background:var(--demo-blue)}
.btn-demo.secondary{background:var(--demo-grey);width:69px;justify-content:center}

.board{left:547px;top:10px;width:235px;height:356px;background:var(--board);border:1px solid #463a63;border-radius:6px}
.board .mark{position:absolute;left:10px;top:6px;display:flex;align-items:center;gap:6px;font-size:35px;font-weight:700;color:var(--accent);line-height:1}
.board .mark i{width:30px;height:30px;border-radius:50%;background:var(--text);display:block}
.board .url{position:absolute;left:12px;top:46px;font-size:13px;font-weight:600}
.board ul{position:absolute;left:24px;top:70px;list-style:none;font-size:13px;letter-spacing:-.2px}
.board li{height:28px;white-space:nowrap}
.board li b{font-weight:400;margin-left:8px}

.footer{left:0;top:984px;width:1200px;height:163px;background:var(--bg-footer)}
.footer nav{position:absolute;left:0;width:1200px;top:24px;display:flex;justify-content:center;gap:38px;text-align:center}
.footer nav a{color:var(--text);text-decoration:none;font-size:14px}
.footer nav small{font-family:"Kanit",sans-serif;font-size:12px;display:block}
.footer .copy{position:absolute;left:0;width:1200px;top:91px;text-align:center;font-size:14px}
</style>
</head>
<body>

<div class="abs topbar">
  <div class="abs contact">+953 014 7720 318 care@mirvexa3.com</div>
  <div class="abs social" aria-label="social links"><span></span><span></span><span></span><span></span></div>
</div>

<header class="abs header">
  <div class="abs brand">
    <div class="mark"><i></i>MIRVEXA3</div>
    <div class="url">www.mirvexa3.com</div>
  </div>
  <nav class="abs nav">
    <a style="width:78px"><span class="num">01</span><span class="en">HOME</span><span class="th">หน้า หลัก</span></a>
    <a style="width:96px"><span class="num">02</span><span class="en">REGISTER</span><span class="th">สมัครสมาชิก</span></a>
    <a style="width:102px"><span class="num">03</span><span class="en">PROMOTION</span><span class="th">โปรโมชั่</span></a>
    <a style="width:86px"><span class="num">04</span><span class="en">BANKING</span><span class="th">ฝาก - ถอน</span></a>
    <a style="width:76px"><span class="num">05</span><span class="en">LIVE</span><span class="th">ดูบอลสด</span></a>
    <a style="width:88px"><span class="num">06</span><span class="en">CONTACT</span><span class="th">ติดต่อเรา</span></a>
  </nav>
</header>

<section class="abs hero" role="img" aria-label="Casino floor with rows of slot machines under purple and red lights">
  <div class="abs hero-copy">
    <div class="th">ข้อเสนอการฝากเงินครั้งแรก</div>
    <div class="en">The First Deposit Offer 30%</div>
    <span class="btn-signin">Sign In</span>
  </div>
</section>

<form class="abs register">
  <h2>สมัครสมาชิก</h2>
  <div class="field" style="top:42px">ชื่อ - สกุล</div>
  <div class="field" style="top:73px">เบอร์โทรที่สามารถติดต่อ</div>
  <div class="field" style="top:104px">Line ID ที่สามารถติดต่อ</div>
  <div class="submit">Submit<small>เสนอ</small></div>
  <div class="forgot">Forgot Password ? <span>/</span> ลืมรหัสผ่าน ?</div>
</form>

<div class="abs cta" style="top:691px">SignUp Now<small>สมัครตอนนี้เลย</small></div>
<div class="abs cta" style="top:781px">Game Demo<small>การสาธิตเกม</small></div>

<section class="abs games">
  <article class="abs game-card" style="top:10px">
    <div class="thumb" role="img" aria-label="Hand holding four aces playing cards"></div>
    <span class="num">01</span><span class="th">สมบัติ</span><span class="tag">TREASURE</span>
    <p>Lorem Ipsum is simply dummy text of the printing and typesetting industry. Lorem Ipsum has been the industry's standard dummy text</p>
    <div class="btns"><span class="btn-demo primary"><svg width="12" height="13" viewBox="0 0 12 13"><path d="M1 1l10 5.5L1 12z" fill="#fff"/></svg>Demo</span><span class="btn-demo secondary">Demo</span></div>
  </article>
  <article class="abs game-card" style="top:177px">
    <div class="thumb" role="img" aria-label="Hand holding four aces playing cards"></div>
    <span class="num">01</span><span class="th">สมบัติ</span><span class="tag">TREASURE</span>
    <p>Lorem Ipsum is simply dummy text of the printing and typesetting industry. Lorem Ipsum has been the industry's standard dummy text</p>
    <div class="btns"><span class="btn-demo primary"><svg width="12" height="13" viewBox="0 0 12 13"><path d="M1 1l10 5.5L1 12z" fill="#fff"/></svg>Demo</span><span class="btn-demo secondary">Demo</span></div>
  </article>

  <aside class="abs board">
    <div class="mark"><i></i>MIRVEXA3</div>
    <div class="url">www.mirvexa3.com</div>
    <ul>
      <li>12:53:19 user22b251xx<b>$ 300.00</b></li>
      <li>12:53:19 user22b251xx<b>$ 300.00</b></li>
      <li>12:53:19 user22b251xx<b>$ 300.00</b></li>
      <li>12:53:19 user22b251xx<b>$ 300.00</b></li>
      <li>12:53:19 user22b251xx<b>$ 300.00</b></li>
      <li>12:53:19 user22b251xx<b>$ 300.00</b></li>
      <li>12:53:19 user22b251xx<b>$ 300.00</b></li>
      <li>12:53:19 user22b251xx<b>$ 300.00</b></li>
      <li>12:53:19 user22b251xx<b>$ 300.00</b></li>
      <li>12:53:19 user22b251xx<b>$ 300.00</b></li>
    </ul>
  </aside>
</section>

<footer class="abs footer">
  <nav>
    <a>Home<small>หน้า หลัก</small></a>
    <a>Register<small>สมัครสมาชิก</small></a>
    <a>Promotion<small>โปรโมชั่</small></a>
    <a>Banking<small>ฝาก - ถอน</small></a>
    <a>Live<small>ดูบอลสด</small></a>
    <a>Contact<small>ติดต่อเรา</small></a>
  </nav>
  <div class="copy">Copyright ©2018 Copyright © MIRVEXA3.COM All Rights Reserved.</div>
</footer>

</body>
</html>
```